EdTech startup needs web (& logo?) redesign

LecternHop.com is a collection of fun online tools designed to help instructors in higher education (i.e. university) build a sense of community in the classroom and enable "active learning." We have spent most of our energy on developing functionality and would love to have some real designers contribute their ideas. Everything (logos, color scheme, images, etc.) is up for grabs, but the winning design should be bootstrap friendly. We are currently using the "Megaframe" template, but are open to others. That being said, we are less interested in getting great code than a great design. Websites we admire include voteswirl.com, workmesh.com, and http://skins.fetchframe.com/products/application

Pages we are particularly interested in ideas for include: homepage, shuffle pick, the grabber, and extra tambourine. The latter three currently use images that probably can't go mainstream.

If you want to participate in the contest we would love for you to check out the site first. In order to enable this, we have set up a fictional class (LPHX 207-3 - Beta Website Redesign). Once you create an account at www.lecternhop.com, you just enter the super-secret invite code "e9a27b41" to add yourself to the class.

Attached our some files that were used to inspire our current design. Feel free to use or ignore them as you see fit. Thanks!

Target Market(s)

college students and their instructors

Industry/Entity Type

Education

Coding

Coded - Design and coding required

Number of Pages Required

4 page

Colors
0355a3
33a6d7
cee9f5

Requirements
Must have
• cool, fun design that is boostrap friendly.
Nice to have
• I like blue, but an open to other color themes.
Should not have
• ?

```html
<!DOCTYPE html>
<html lang="en">
<head>
<meta charset="utf-8">
<title>Lectern Hop – Rubrics</title>
<link rel="stylesheet" href="https://fonts.googleapis.com/css2?family=Archivo+Black&family=Open+Sans:wght@400;600&display=swap">
<style>
  :root {
    --hero-dark: #2b2d31;
    --hero-mid: #55585e;
    --hero-light: #8a8d92;
    --white: #ffffff;
    --accent-blue: #5a9fd4;
    --button-blue: #5a9fd4;
    --accent-red: #d9503f;
    --text-body: #444444;
    --footer-red: #d84f3e;
    --icon-tone: rgba(255, 255, 255, 0.35);
  }
  * { box-sizing: border-box; margin: 0; padding: 0; }
  html, body {
    width: 1200px;
    height: 600px;
    overflow: hidden;
    background: var(--white);
  }
  .page {
    position: relative;
    width: 1200px;
    height: 600px;
    font-family: "Open Sans", Arial, sans-serif;
  }

  /* Hero */
  .hero {
    position: absolute;
    left: 0; top: 0;
    width: 1200px;
    height: 297px;
  }
  .hero-photo {
    position: absolute;
    inset: 0;
    background:
      radial-gradient(ellipse 260px 150px at 560px 200px, var(--hero-light), transparent 70%),
      linear-gradient(100deg, var(--hero-dark) 0%, var(--hero-mid) 35%, var(--hero-mid) 60%, var(--hero-dark) 100%);
  }
  .hero-shade {
    position: absolute;
    inset: 0;
    background: rgba(0, 0, 0, 0.25);
  }
  .brand {
    position: absolute;
    left: 186px;
    top: 40px;
    font-family: "Archivo Black", "Arial Black", sans-serif;
    font-size: 20px;
    line-height: 28px;
    color: var(--white);
  }
  .nav-actions {
    position: absolute;
    left: 882px;
    top: 35px;
    display: flex;
    gap: 9px;
  }
  .signup-button {
    width: 83px;
    height: 37px;
    background: var(--button-blue);
    color: var(--white);
    font-size: 14px;
    font-weight: 600;
    line-height: 37px;
    text-align: center;
    text-transform: uppercase;
    border-radius: 2px;
  }
  .menu-button {
    width: 37px;
    height: 37px;
    background: var(--accent-red);
    border-radius: 2px;
    display: flex;
    align-items: center;
    justify-content: center;
  }
  .hero-title {
    position: absolute;
    left: 0; right: 0;
    top: 153px;
    text-align: center;
    font-family: "Archivo Black", "Arial Black", sans-serif;
    font-size: 37px;
    line-height: 46px;
    color: var(--white);
    letter-spacing: 0.5px;
  }

  /* Content */
  .tool-intro {
    position: absolute;
    left: 0; right: 0;
    top: 345px;
    text-align: center;
  }
  .tool-heading {
    font-family: "Archivo Black", "Arial Black", sans-serif;
    font-size: 22px;
    line-height: 30px;
    color: var(--accent-blue);
    margin-bottom: 4px;
  }
  .tool-description {
    font-size: 14px;
    line-height: 17.5px;
    color: var(--text-body);
  }

  /* Footer */
  .site-footer {
    position: absolute;
    left: 0; top: 488px;
    width: 1200px;
    height: 112px;
    background: var(--footer-red);
    text-align: center;
  }
  .social-links {
    display: flex;
    justify-content: center;
    gap: 5px;
    margin-top: 28px;
  }
  .social-link {
    width: 20px;
    height: 20px;
    border-radius: 3px;
    background: var(--icon-tone);
  }
  .copyright {
    margin-top: 12px;
    font-size: 11px;
    line-height: 16px;
    color: var(--white);
  }
</style>
</head>
<body>
<div class="page">
  <header class="hero">
    <div class="hero-photo" role="img" aria-label="Photo of two people in business suits shaking hands"></div>
    <div class="hero-shade"></div>
    <div class="brand">Lectern Hop</div>
    <div class="nav-actions">
      <div class="signup-button">Sign up</div>
      <div class="menu-button" aria-label="Menu">
        <svg width="20" height="16" viewBox="0 0 20 16">
          <rect x="0" y="1" width="20" height="3" rx="1.5" fill="#ffffff"/>
          <rect x="0" y="6.5" width="20" height="3" rx="1.5" fill="#ffffff"/>
          <rect x="0" y="12" width="20" height="3" rx="1.5" fill="#ffffff"/>
        </svg>
      </div>
    </div>
    <h1 class="hero-title">HELLO-RUBRICS</h1>
  </header>

  <main class="tool-intro">
    <h2 class="tool-heading">Rubrics</h2>
    <p class="tool-description">
      (comingSummer 2016) Rubrics are a great tool - both for providing guidence and feedback<br>
      This tool lets you create your own rubrics to use for assignments (self/peer evals for example).<br>
      Also, you can search a database of existing rubrics to use as a starting point.
    </p>
  </main>

  <footer class="site-footer">
    <div class="social-links">
      <span class="social-link" aria-label="Social link"></span>
      <span class="social-link" aria-label="Social link"></span>
      <span class="social-link" aria-label="Social link"></span>
      <span class="social-link" aria-label="Social link"></span>
      <span class="social-link" aria-label="Social link"></span>
    </div>
    <p class="copyright">© Copyright 2016, lecternhop.com</p>
  </footer>
</div>
</body>
</html>
```